Design a menu for health restaurant

A health food restaurant in Los Angeles is seeking menu design. Our foods are made from scratch using whole ingredients.
Name: Grove Pantry
Address: 1000 E 60th StLos Angeles, CA 90347
Website: www.GrovePantry-example.com
We are looking for a clean and simple menu. Brand colors are white/tan, green and orange.

Please see attached excel with menu items and logo. We do not yet have prices.

Colors
f78f20
9bcb3c
ffffff
fff3d1

Requirements
Must have
• Easy to read.
Trifold menu design (front and back).
VEGAN, VEGETARIAN, GLUTEN FREE, CONTAINS NUTS symbols.
Logo.
Nice to have
• Incorporate brand colors, but still be easy to read.
We would like to use the Belco font (attached) if it works. If not we are open to a similar font that is easy to read.

Please see attached images.
We like the images and headers of OPTION 1. Would like something similar in trifold format.
We like the clean fonts of OPTION 2.

```html
<!DOCTYPE html>
<html lang="en">
<head>
<meta charset="utf-8">
<title>Grove Pantry — Menu</title>
<link rel="stylesheet" href="https://fonts.googleapis.com/css2?family=Bowlby+One&family=Signika:wght@400;500&display=swap">
<style>
:root{
  --orange:#f78f20;
  --orange-dk:#ee7d10;
  --green:#9bcb3c;
  --cream:#fff3d1;
  --white:#ffffff;
  --frame:#5c5c5c;
  --gap:#d9d9d9;
}
*{box-sizing:border-box;margin:0;padding:0}
html,body{width:759px;height:1200px;overflow:hidden}
body{background:var(--frame);position:relative;font-family:"Signika",sans-serif;color:var(--orange)}
.sheet{position:absolute;left:5px;width:748px;background:var(--white)}
.sheet--front{top:8px;height:582px}
.sheet--back{top:592px;height:596px}
.divider-band{position:absolute;left:5px;width:748px;top:590px;height:2px;background:var(--gap)}
.section{position:absolute;border:1px dashed var(--green);padding:12px 10px 6px}
.section__title{position:absolute;top:-9px;left:10px;z-index:2;background:var(--white);padding:0 4px;font-family:"Bowlby One",sans-serif;font-size:12.5px;letter-spacing:.3px;line-height:17px;white-space:nowrap;color:var(--orange)}
.item{padding:4px 0 5px;border-bottom:1px dotted #cfe6a0}
.item:last-child{border-bottom:none}
.item__name{font-size:9px;font-weight:500;line-height:11px;display:flex;align-items:center;gap:2px}
.item__desc{font-size:6.6px;line-height:10px;color:var(--orange);margin-top:1px}
.price{float:right;font-size:6.8px;color:var(--green);font-weight:500}
.ic{width:9px;height:9px;flex:none}
.photo{position:absolute;border-radius:2px;z-index:1}
.photo--salad{background:radial-gradient(circle at 50% 50%,#7aa043 0%,#c4553b 45%,#eef0ea 72%)}
.photo--soup{background:radial-gradient(circle at 50% 50%,#c27a2a 0%,#d99a48 45%,#f1ede6 70%)}
.photo--burger{background:radial-gradient(circle at 45% 50%,#b8782f 0%,#8fae4a 50%,#eeece6 75%)}
.photo--chips{background:radial-gradient(circle at 40% 40%,#3b3a3e 0%,#a6c46a 55%,#f2f1ed 78%)}
.photo--smoothie{background:linear-gradient(#c9a3d6,#8a5fa1);border-radius:3px 3px 8px 8px}
.photo--drink{background:linear-gradient(#f6b3b6,#e65a6a);border-radius:3px 3px 7px 7px}
.brand{position:absolute;left:5px;top:8px;width:150px;height:150px}
.brand__name{position:absolute;left:43px;top:71px;width:90px;text-align:center;font-family:"Signika",sans-serif;font-weight:500;font-size:13px;line-height:15px;color:var(--white)}
.tag{position:absolute;background:var(--orange);color:var(--white);font-size:6.6px;line-height:8px;padding:2px 12px 2px 14px;white-space:nowrap;clip-path:polygon(0 0,100% 0,94% 50%,100% 100%,0 100%)}
.tag svg{position:absolute;left:3px;top:50%;transform:translateY(-50%);width:8px;height:8px}
.legend{position:absolute;left:36px;top:504px;width:209px;height:50px;background:var(--cream);border:1px dashed var(--green);display:grid;grid-template-columns:1fr 1fr;align-items:center;justify-items:center;padding:4px 10px}
.legend span{display:flex;align-items:center;gap:3px;font-size:7px;font-weight:500;letter-spacing:.3px}
.legend .g{color:var(--green)}
</style>
</head>
<body>
<svg width="0" height="0" style="position:absolute" aria-hidden="true">
  <defs>
    <symbol id="i-vegan" viewBox="0 0 10 10"><circle cx="5" cy="5" r="4.6" fill="#9bcb3c"/><path d="M3 7c0-3 2-4 4.5-4.3C7.3 5.5 6 7 3 7z" fill="#fff"/></symbol>
    <symbol id="i-veg" viewBox="0 0 10 10"><circle cx="5" cy="5" r="4.3" fill="none" stroke="#9bcb3c" stroke-width=".9"/><path d="M3 3l2 4.3L7.2 2.6" fill="none" stroke="#9bcb3c" stroke-width="1.1"/></symbol>
    <symbol id="i-gf" viewBox="0 0 10 10"><circle cx="5" cy="5" r="4.3" fill="none" stroke="#f78f20" stroke-width=".9"/><path d="M5 8V3M5 4.5l-1.5-1M5 4.5l1.5-1M5 6l-1.5-1M5 6l1.5-1M2.2 7.8l5.6-5.6" fill="none" stroke="#f78f20" stroke-width=".8"/></symbol>
    <symbol id="i-nuts" viewBox="0 0 10 10"><circle cx="5" cy="5" r="4.3" fill="none" stroke="#f78f20" stroke-width=".9"/><ellipse cx="5" cy="5.3" rx="1.8" ry="2.4" fill="none" stroke="#f78f20" stroke-width=".8"/></symbol>
  </defs>
</svg>

<div class="sheet sheet--front"></div>
<div class="divider-band"></div>
<div class="sheet sheet--back"></div>

<!-- Front brand corner -->
<svg class="brand" viewBox="0 0 150 150" aria-hidden="true">
  <path d="M0 0h138c6 40-8 86-40 112S28 148 0 150z" fill="#f9a33f"/>
  <circle cx="78" cy="71" r="55" fill="#fff"/>
  <circle cx="78" cy="71" r="47" fill="#f78f20"/>
</svg>
<div class="brand__name">Grove Pantry</div>
<div class="tag" style="left:146px;top:75px">
  <svg viewBox="0 0 10 10"><path d="M5 1a3 3 0 0 1 3 3c0 2.3-3 5-3 5S2 6.3 2 4a3 3 0 0 1 3-3z" fill="#fff"/><circle cx="5" cy="4" r="1.1" fill="#f78f20"/></svg>
  2417 W 38th Ave<br>Los Angeles, CA 90347
</div>
<div class="tag" style="left:136px;top:112px">
  <svg viewBox="0 0 10 10"><circle cx="5" cy="5" r="4" fill="none" stroke="#fff"/><path d="M1 5h8M5 1c-2 2.5-2 5.5 0 8M5 1c2 2.5 2 5.5 0 8" fill="none" stroke="#fff" stroke-width=".7"/></svg>
  www.GrovePantry-example.com
</div>

<!-- BREAKFAST -->
<section class="section" style="left:36px;top:162px;width:209px;height:329px">
  <h2 class="section__title">BREAKFAST</h2>
  <div class="item"><div class="item__name">Pastries <svg class="ic"><use href="#i-veg"/></svg></div><div class="item__desc">Croissant (regular, almond, chocolate)<br>Blueberry Muffin<br>Superseed Cookie <span class="price">11.99</span></div></div>
  <div class="item"><div class="item__name">Parfait <svg class="ic"><use href="#i-veg"/></svg></div><div class="item__desc">Fresh strawberries and blueberries on yogurt<br>and muesli and topped with honey drizzle.</div></div>
  <div class="item"><div class="item__name">Avocado Super Toast <svg class="ic"><use href="#i-vegan"/></svg></div><div class="item__desc">Avocado Mash, Tomato, Basil, Ground Flax,<br>Hemp Seed, Chickpeas, and Moringa Powder<br>on Whole Wheat Bread.</div></div>
  <div class="item"><div class="item__name">Brunch Burger</div><div class="item__desc">House seasoned beef burger topped with<br>an over medium egg, red leaf lettuce, tomato,<br>housemade pickles and Pantry Sauce on a bun.</div></div>
  <div class="item"><div class="item__name">Breakfast Sammy <svg class="ic"><use href="#i-vegan"/></svg></div><div class="item__desc">Fresh strawberries and blueberries on yogurt<br>and muesli and topped with honey drizzle.</div></div>
  <div class="item"><div class="item__name">AM Burrito <svg class="ic"><use href="#i-veg"/></svg></div><div class="item__desc">Scrambled eggs, onion, red bell pepper,<br>black beans, housemade salsa, yogurt, and pepper<br>jack cheese in a tortilla.</div></div>
</section>
<div class="photo photo--burger" style="left:184px;top:143px;width:53px;height:40px" role="img" aria-label="Photo of the breakfast burger"></div>

<div class="legend">
  <span class="g"><svg class="ic"><use href="#i-vegan"/></svg>VEGAN</span>
  <span class="g"><svg class="ic"><use href="#i-veg"/></svg>VEGETARIAN</span>
  <span><svg class="ic"><use href="#i-gf"/></svg>GLUTEN FREE</span>
  <span><svg class="ic"><use href="#i-nuts"/></svg>CONTAINS NUTS</span>
</div>

<!-- BOWLS -->
<section class="section" style="left:273px;top:86px;width:213px;height:364px">
  <h2 class="section__title">BOWLS</h2>
  <div class="item"><div class="item__name">Southwest Bowl <svg class="ic"><use href="#i-gf"/></svg><svg class="ic"><use href="#i-nuts"/></svg></div><div class="item__desc">Your choice of protein with corn, black beans,<br>red onions, almonds and avocado over quinoa<br>with lime hot sauce.</div></div>
  <div class="item"><div class="item__name">Chimi Bowl <svg class="ic"><use href="#i-gf"/></svg></div><div class="item__desc">Your choice of protein with red bell pepper, mushrooms,<br>zucchini, squash, onion, cherry tomatoes and<br>fresh herb chimichurri on wild and brown rice.</div></div>
  <div class="item"><div class="item__name">Soba Noodle Bowl</div><div class="item__desc">Your choice of protein with spinach, snow peas,<br>roasted carrots, red bell pepper, cilantro, sesame seeds<br>and ginger lime sauce over soba noodles.</div></div>
  <div class="item"><div class="item__name">Hollywood Bowl <svg class="ic"><use href="#i-gf"/></svg></div><div class="item__desc">Your choice of protein with broccoli, roasted corn,<br>cherry tomatoes, basil, pepitas, flax seeds and<br>lemon juice on wild and brown rice.</div></div>
  <div class="item"><div class="item__name">Pantry Bowl <svg class="ic"><use href="#i-gf"/></svg></div><div class="item__desc">Your choice of protein with roasted chickpeas and<br>cauliflower, zesty fennel salad and citrus yogurt.</div></div>
  <div class="item"><div class="item__name">Buddha Bowl</div><div class="item__desc">Your choice of protein with corn, red kale, sweet potatoes,<br>red cabbage, parsley, oregano, hummus, and farro.</div></div>
  <div class="item"><div class="item__name">Chili Rice Bowl <svg class="ic"><use href="#i-gf"/></svg></div><div class="item__desc">Chicken, onions, bell peppers, jalapeños, black &amp;<br>kidney beans, and tomato over brown rice.</div></div>
</section>
<div class="photo photo--salad" style="left:359px;top:41px;width:58px;height:43px" role="img" aria-label="Photo of a green bowl with radish"></div>
<div class="photo photo--salad" style="left:422px;top:54px;width:51px;height:50px" role="img" aria-label="Photo of a protein bowl"></div>
<div class="photo photo--salad" style="left:273px;top:457px;width:68px;height:69px" role="img" aria-label="Photo of a roasted vegetable bowl"></div>
<div class="photo photo--salad" style="left:345px;top:457px;width:68px;height:69px" role="img" aria-label="Photo of a grain bowl with citrus"></div>
<div class="photo photo--salad" style="left:417px;top:457px;width:68px;height:69px" role="img" aria-label="Photo of a leafy salad bowl"></div>

<!-- WRAPS -->
<section class="section" style="left:509px;top:50px;width:214px;height:161px">
  <h2 class="section__title">WRAPS</h2>
  <div class="item"><div class="item__name">Rancher's Wrap</div><div class="item__desc">Tomato, red onion, hard boiled egg, avocado,<br>feta cheese, microgreens, romaine, grilled chicken &amp;<br>Ranch dressing in a grilled wrap.</div></div>
  <div class="item"><div class="item__name">Vegan Tuna Wrap <svg class="ic"><use href="#i-vegan"/></svg></div><div class="item__desc">Vegan tuna, romaine, avocado, celery, shallot, &amp; oregano<br>with Herbalicious Sauce in a whole grain wrap.</div></div>
  <div class="item"><div class="item__name">Vegetarian Wrap <svg class="ic"><use href="#i-veg"/></svg></div><div class="item__desc">Roasted chickpeas, romaine, avocado, red bell pepper,<br>shaved carrots, cucumber, spinach, basil, black beans &amp;<br>feta with lemon-hummus in a sprouted 7-grain wrap.</div></div>
</section>

<!-- SOUPS -->
<section class="section" style="left:509px;top:231px;width:214px;height:153px">
  <h2 class="section__title">SOUPS</h2>
  <div class="item"><div class="item__name">Chicken Noodle <svg class="ic"><use href="#i-gf"/></svg></div><div class="item__desc">Chicken, egg noodles, root vegetables, oregano &amp;<br>peppercorns.</div></div>
  <div class="item"><div class="item__name">Pantry Chili <svg class="ic"><use href="#i-gf"/></svg></div><div class="item__desc">Chicken, onions, bell peppers, jalapeños, black &amp;<br>kidney beans, and tomato.</div></div>
  <div class="item"><div class="item__name">Seasonal Rotating <svg class="ic"><use href="#i-vegan"/></svg><svg class="ic"><use href="#i-nuts"/></svg></div><div class="item__name">(Butternut Squash Soup</div><div class="item__desc">Butternut squash blended with warm spices, and<br>coconut milk.</div></div>
</section>
<div class="photo photo--soup" style="left:680px;top:219px;width:37px;height:30px" role="img" aria-label="Photo of a bowl of soup"></div>

<!-- COMBOS -->
<section class="section" style="left:509px;top:402px;width:214px;height:127px">
  <h2 class="section__title">COMBOS</h2>
  <div class="item"><div class="item__name">Soup + Salad</div><div class="item__desc">Your choice of soup and side salad.<br>16oz soup + 38oz salad</div></div>
  <div class="item"><div class="item__name">Avo Toast Combo</div><div class="item__desc">Half avocado toast and your choice of soup. 16oz</div></div>
  <div class="item"><div class="item__name">Soup + Sammy</div><div class="item__desc">Your choice of soup and sandwich.<br>16oz soup + Sandwich</div></div>
</section>
<div class="photo photo--soup" style="left:642px;top:395px;width:37px;height:33px" role="img" aria-label="Photo of squash soup"></div>
<div class="photo photo--salad" style="left:683px;top:395px;width:37px;height:33px" role="img" aria-label="Photo of a side salad"></div>

<!-- BURGERS -->
<section class="section" style="left:33px;top:652px;width:214px;height:297px">
  <h2 class="section__title">BURGERS N' SAMMIES</h2>
  <div class="item"><div class="item__name">Air Fried Chicken Sammy</div><div class="item__desc">Air fried chicken breast topped with red leaf lettuce,<br>tomato, house made pickles and Pantry Sauce on a<br>bun served with choice of salad of fries.</div></div>
  <div class="item"><div class="item__name">Grilled Chicken Sammy</div><div class="item__desc">Grilled chicken topped with guacamole, red leaf lettuce,<br>tomato, house made pickles and Pantry Sauce.<br>Served with regular fries or side salad.</div></div>
  <div class="item"><div class="item__name">Classic Beef Burger</div><div class="item__desc">House seasoned beef burger topped with red leaf lettuce,<br>tomato, cheddar cheese, house made pickles and<br>Pantry Sauce on a bun served with choice of<br>salad of fries.</div></div>
  <div class="item"><div class="item__name">Black Bean Pine Nut Burger <svg class="ic"><use href="#i-vegan"/></svg><svg class="ic"><use href="#i-nuts"/></svg></div><div class="item__desc">House made black bean pine nut burger topped with<br>red leaf lettuce, tomato, house made pickles and mustard<br>aioli on a bun served with choice of salad of fries.</div></div>
  <div class="item"><div class="item__name">Salmon Burger</div><div class="item__desc">House made salmon burger topped with red leaf lettuce,<br>tomato, house made pickles and Pantry yogurt on a<br>bun served with choice of salad of fries.</div></div>
</section>
<div class="photo photo--burger" style="left:212px;top:636px;width:34px;height:32px" role="img" aria-label="Photo of a burger with salad"></div>

<!-- SNACKS -->
<section class="section" style="left:33px;top:969px;width:214px;height:168px">
  <h2 class="section__title">SNACKS N' SIDES</h2>
  <div class="item"><div class="item__name">Fries <svg class="ic"><use href="#i-vegan"/></svg><svg class="ic"><use href="#i-gf"/></svg></div><div class="item__desc">Hand cut air-fries with house seasonings.<br>Choose regular or sweet potato fries.</div></div>
  <div class="item"><div class="item__name">Side Salad</div><div class="item__desc">Your choice of House, Golden Beet, Mediterranean,<br>or Vegan Chef side salad. (24oz)</div></div>
  <div class="item"><div class="item__name">Guac + Chips <svg class="ic"><use href="#i-vegan"/></svg><svg class="ic"><use href="#i-gf"/></svg></div><div class="item__desc">Guacamole with blue corn tortilla chips.</div></div>
  <div class="item"><div class="item__name">Hummus + Chips <svg class="ic"><use href="#i-vegan"/></svg><svg class="ic"><use href="#i-gf"/></svg></div><div class="item__desc">Hummus with blue corn tortilla chips.</div></div>
</section>

<!-- SALADS -->
<section class="section" style="left:272px;top:651px;width:214px;height:279px">
  <h2 class="section__title">SALADS</h2>
  <div class="item"><div class="item__name">Avocado, Golden Beet, and <svg class="ic"><use href="#i-veg"/></svg><svg class="ic"><use href="#i-gf"/></svg></div><div class="item__name">Cranberry Salad</div><div class="item__desc">Gold beets, avocado, dried cranberries, watermelon radish,<br>red kale, romaine, mixed greens, and pepitas served with<br>Golden Buddha dressing.</div></div>
  <div class="item"><div class="item__name">Burrata Salad <svg class="ic"><use href="#i-veg"/></svg><svg class="ic"><use href="#i-gf"/></svg></div><div class="item__desc">Tomato, melon, shredded basil, balsamic glaze,<br>fresh cracked pepper, and olive oil with burrata.</div></div>
  <div class="item"><div class="item__name">Mediterranean Salad <svg class="ic"><use href="#i-veg"/></svg><svg class="ic"><use href="#i-gf"/></svg></div><div class="item__desc">Cucumbers, Kalamata olives, cherry tomatoes, parsley,<br>tricolor quinoa, hard-boiled egg, and hummus on mixed<br>greens, romaine, and red cabbage with lemon-olive<br>oil dressing.</div></div>
  <div class="item"><div class="item__name">Vegan Chef Salad <svg class="ic"><use href="#i-vegan"/></svg><svg class="ic"><use href="#i-gf"/></svg><svg class="ic"><use href="#i-nuts"/></svg></div><div class="item__desc">Roasted potatoes and carrots, chickpeas, avocado,<br>microgreens and walnuts on mixed greens, romaine, and<br>red kale with vegan ranch.</div></div>
  <div class="item"><div class="item__name">Rancher's Salad <svg class="ic"><use href="#i-veg"/></svg><svg class="ic"><use href="#i-gf"/></svg></div><div class="item__desc">Tomato, red onion, hard boiled egg, avocado, feta cheese,<br>microgreens, and grilled chicken on romaine with<br>Ranch dressing.</div></div>
</section>
<div class="photo photo--salad" style="left:433px;top:638px;width:45px;height:45px" role="img" aria-label="Photo of a mixed green salad"></div>

<!-- DESSERTS -->
<section class="section" style="left:272px;top:960px;width:214px;height:166px">
  <h2 class="section__title">DESSERTS</h2>
  <div class="item"><div class="item__name">Date Coffee Cake <svg class="ic"><use href="#i-vegan"/></svg><svg class="ic"><use href="#i-nuts"/></svg></div><div class="item__desc">Signature date coffee cake with walnuts.</div></div>
  <div class="item"><div class="item__name">Fruit + Spices <svg class="ic"><use href="#i-vegan"/></svg><svg class="ic"><use href="#i-gf"/></svg></div><div class="item__desc">Strawberry, pineapple, green apple, orange, and<br>blueberries with lime and chili seasoning.</div></div>
  <div class="item"><div class="item__name">Cookies <svg class="ic"><use href="#i-veg"/></svg></div><div class="item__desc">Your choice of Chocolate Chip or Double<br>Chocolate Chip fresh baked cookie.</div></div>
  <div class="item"><div class="item__name">Pantry Chocolate Mousse <svg class="ic"><use href="#i-vegan"/></svg><svg class="ic"><use href="#i-gf"/></svg></div><div class="item__desc">Served with grated dark chocolate.</div></div>
</section>
<div class="photo photo--chips" style="left:437px;top:943px;width:44px;height:45px" role="img" aria-label="Photo of chips with guacamole"></div>

<!-- SMOOTHIES -->
<section class="section" style="left:512px;top:644px;width:214px;height:127px">
  <h2 class="section__title">SMOOTHIES</h2>
  <div class="item"><div class="item__name">Green Machine Smoothie <svg class="ic"><use href="#i-vegan"/></svg><svg class="ic"><use href="#i-gf"/></svg><svg class="ic"><use href="#i-nuts"/></svg></div><div class="item__desc">Romaine, spinach, banana, mango, pineapple,<br>flaxmilk, spirulina, almond butter <span class="price">6.99</span></div></div>
  <div class="item"><div class="item__name">Acai Smoothie <svg class="ic"><use href="#i-vegan"/></svg><svg class="ic"><use href="#i-gf"/></svg><svg class="ic"><use href="#i-nuts"/></svg></div><div class="item__desc">Acai, blueberries, banana, pineapple, Macqui berry,<br>flaxmilk, almond butter</div></div>
  <div class="item"><div class="item__name">Mango Smoothie <svg class="ic"><use href="#i-vegan"/></svg><svg class="ic"><use href="#i-nuts"/></svg></div><div class="item__desc">Mango, flaxmilk, banan, hemp seeds</div></div>
</section>
<div class="photo photo--smoothie" style="left:686px;top:629px;width:23px;height:33px" role="img" aria-label="Photo of a purple smoothie cup"></div>

<!-- DRINKS -->
<section class="section" style="left:512px;top:789px;width:214px;height:365px">
  <h2 class="section__title">DRINKS</h2>
  <div class="item"><div class="item__name">Coffee</div><div class="item__desc">We proudly serve Ridgeline Coffee, a local roaster.</div></div>
  <div class="item"><div class="item__name">Power Date Shake <svg class="ic"><use href="#i-vegan"/></svg><svg class="ic"><use href="#i-gf"/></svg></div><div class="item__desc">Ice-blended energy smoothie featuring dates<br>and coffee.</div></div>
  <div class="item"><div class="item__name">Heart Beet Juice <svg class="ic"><use href="#i-vegan"/></svg><svg class="ic"><use href="#i-gf"/></svg></div><div class="item__desc">Red beet, apple, carrot, ginger, parsley, and lemon.</div></div>
  <div class="item"><div class="item__name">Green Leafy Juice <svg class="ic"><use href="#i-vegan"/></svg><svg class="ic"><use href="#i-gf"/></svg></div><div class="item__desc">Spinach, kale, cucumber, apple, and oranges.</div></div>
  <div class="item"><div class="item__name">Orange Turmeric Juice <svg class="ic"><use href="#i-vegan"/></svg><svg class="ic"><use href="#i-gf"/></svg></div><div class="item__desc">Turmeric, ginger, lemon, carrot, and orange topped<br>with cracked black pepper.</div></div>
  <div class="item"><div class="item__name">Fireshot <svg class="ic"><use href="#i-vegan"/></svg><svg class="ic"><use href="#i-gf"/></svg></div><div class="item__desc">Ginger and lemon shot topped with cayenne.</div></div>
  <div class="item"><div class="item__name">Lemonade</div><div class="item__desc">House Made Lemonade. Choice of unsweetened or agave<br>sweetened in Regular, Raspberry, and Lavender flavors.</div></div>
  <div class="item"><div class="item__name">Tea</div><div class="item__desc">Hot or iced</div></div>
  <div class="item"><div class="item__name">Bottled Drinks</div><div class="item__desc">Hillside kombucha (Harmony Trilogy, Harmony Gingerberry,<br>Harmony Mango) Brightwater (Orange Mango, Lemon,<br>Grapefruit) Palm Grove Original Sparkling Water (Evermore)<br>Still Water (Evermore)</div></div>
</section>
<div class="photo photo--drink" style="left:597px;top:778px;width:21px;height:31px" role="img" aria-label="Photo of a pink iced drink"></div>
</body>
</html>
```